Medical Internet Marketing Company Needs a Site!

We need a new, fresh website for our search engine optimization and social media marketing company. We specialize in helping medical practices, doctors, physicians, and hospitals with their online presence and web ranking. The site should lean towards being suited for these audiences.

We have several examples of website that we like as well as things that we like about them.

Here are sites that we enjoy.

www.brightwavelab.com

It's a good design for the site all around. The videos, buttons, and images are all excellent. They did a fine job.

- We really like their "contact us" side bar and want to include one like it on the secondary pages.

www.corvantis.net

- We don't like the "thickness" of the top navigation bar.
- We like the page colors, easy navigation, and big call to action phone number in the top right corner.

http://www.teluvo.com/

Out of all the examples provided, Teluvo is our favorite and closest look and style to what we are looking for.

- We really like the openness of the design, such as space between the text and background.

- We want a price page in a style very similar to their pricing page with the services listed and check-marks, etc. although we intend to have multiple service package columns much like Corvantis's SEO pricing page.

- The way the video fits into the home page header is very organized, simple, and attention grabbing. We intend to place a slider with videos here.

- We need a page design that will allow for an image slider like Teluvo's Features page.

Here's a great example of a medical internet marketing website: http://www.dermaplex.com/

Target Market(s)

Our target market is doctors, typically male and typically 40-45 years old. I

Industry/Entity Type

Marketing

Requirements
Must have
• The homepage should have a slider in the video. Interior pages should have a video in the very top similar to how they do it on www.brightwavelab.com

The top navigation tabs needed are:
- Home
- Solutions
- Resources
- About
- Why Quelvo
- Contact

The sidebar should have a GREAT call to action in it on interior pages.

There should be one interior page that is similar to this - http://www.teluvo.com/pricing/

There needs to be a page with multiple boxes that take up a row of the web page's body. This page will house all the case studies similar to brightwave lab's: http://www.brightwavelab.com/success-stories/case-studies/ The one exception is we want the case studies to be inside of "boxes" instead of between horizontal lines like brightwave lab's.
Nice to have
• Color, professional, and clean. GREAT use of calls to actions.

```html
<!DOCTYPE html>
<html lang="en">
<head>
<meta charset="utf-8">
<title>Quelvo – Search Engine Optimization</title>
<link rel="stylesheet" href="https://fonts.googleapis.com/css2?family=Oswald:wght@300;400&family=Open+Sans:ital,wght@0,300;0,400;0,600;0,700;1,700&family=Play:wght@400;700&family=Noto+Serif&family=Signika:wght@600&display=swap">
<style>
:root{
  --sky-top:#9fcdee;
  --sky-mid:#cfe7f8;
  --sky-pale:#eaf5fc;
  --wave:#8cc3ea;
  --footer:#e4e4e4;
  --ink:#333;
  --ink-soft:#555;
  --orange:#e39a2c;
  --orange-btn:#f5a623;
  --green:#7cb82f;
  --blue:#5bb5e2;
  --deep-blue:#1a73c2;
  --white:#fff;
}
*{box-sizing:border-box;margin:0;padding:0}
html,body{width:960px;height:1200px;overflow:hidden}
body{position:relative;font-family:"Open Sans",sans-serif;color:var(--ink);
  background:linear-gradient(180deg,#6f7275 0,#6f7275 3px,var(--sky-top) 3px,var(--sky-mid) 300px,var(--sky-pale) 520px,#f2f8fc 900px);}
.abs{position:absolute}
.rays{left:0;top:3px;width:960px;height:940px}
/* header */
.brand{left:88px;top:40px;display:flex;align-items:center;gap:12px}
.brand-square{width:60px;height:34px;background:var(--green);border-radius:2px}
.brand-name{font-weight:400;font-size:44px;letter-spacing:3px;color:#8a9096;line-height:1}
.social-top{left:734px;top:11px;display:flex;gap:12px}
.social-top span{width:28px;height:28px;border-radius:50%;display:block}
.nav{left:474px;top:73px;display:flex;font-size:10.5px;font-weight:700}
.nav a{color:#3a3a3a;text-decoration:none;padding:0 12px;border-left:1px solid #aab6c0;line-height:14px}
.nav a:first-child{border-left:none;color:var(--orange)}
/* hero */
.player{left:80px;top:120px;width:370px;height:242px;background:#111;border-radius:4px;border:2px solid #fff;box-shadow:0 1px 4px rgba(0,0,0,.4)}
.player-art{position:absolute;left:3px;top:3px;width:360px;height:200px;background:linear-gradient(135deg,#f4f4f4,#e2e2e2 55%,#cfd8cf)}
.player-bar{position:absolute;left:6px;top:206px;width:340px;height:5px;border-radius:3px;background:#2d6f86}
.player-bar i{display:block;width:94px;height:5px;border-radius:3px;background:#3aa0c6}
.player-x{position:absolute;left:352px;top:204px;width:9px;height:9px;background:#c33;border-radius:2px}
.ctrl{position:absolute;top:220px;height:16px;background:linear-gradient(#fff,#ccc);border-radius:2px;font-size:6.5px;color:#555;display:flex;align-items:center;justify-content:center}
.ctrl-hd{background:linear-gradient(#3ac0f0,#1a8fd0);color:#fff}
.hero-title{left:475px;top:141px;font-family:"Oswald",sans-serif;font-weight:400;font-size:26px;color:#333;letter-spacing:-.2px}
.hero-sub{left:475px;top:205px;font-weight:300;font-size:18.5px;line-height:23.5px;color:#333}
.btn-orange{left:530px;top:299px;width:140px;height:33px;border-radius:4px;background:linear-gradient(#fbbf2c,var(--orange-btn) 60%,#e08a12);color:#222;font-size:14px;display:flex;align-items:center;justify-content:center;box-shadow:0 3px 4px rgba(0,0,0,.12)}
/* content panel */
.panel{left:82px;top:394px;width:796px;height:480px;border-radius:12px 12px 0 0;background:linear-gradient(#fff 70%,rgba(255,255,255,0))}
.section-title{font-family:"Play",sans-serif;font-weight:700;font-size:16.5px;color:#4a4a4a}
.card{top:438px;width:250px;height:110px;border-radius:10px;background:linear-gradient(#f2f2f2,#fff 40%);box-shadow:0 1px 2px rgba(0,0,0,.08)}
.card h3{position:absolute;left:20px;top:6px;font-family:"Play",sans-serif;font-weight:700;font-size:15px}
.card .art{position:absolute;left:12px;top:32px;width:86px;height:58px;border-radius:4px}
.card p{position:absolute;left:108px;top:39px;width:130px;font-size:8.2px;line-height:12.8px;color:#555}
.pill{height:17px;border-radius:9px;color:#fff;font-family:"Play",sans-serif;font-weight:700;font-size:11px;display:flex;align-items:center;justify-content:center}
.card .pill{position:absolute;right:28px;bottom:-6px;width:60px}
.how-art{left:97px;top:625px;width:135px;height:118px;border-radius:4px;background:linear-gradient(135deg,#f6f6f6,#dfe6ec)}
.how-text{left:246px;top:620px;width:365px;font-size:8.4px;line-height:14.4px;color:#555;text-align:justify}
.how-text b{font-style:italic;color:#333}
.news-video{left:642px;top:620px;width:203px;height:130px;background:linear-gradient(#5a5856,#3a3937);border:1px solid #777}
/* cta */
.cta-line{left:109px;top:803px;font-family:"Signika",sans-serif;font-weight:600;font-size:31.5px;color:#8cc63f;white-space:nowrap}
.btn-start{left:660px;top:799px;width:180px;height:46px;background:linear-gradient(#fdfdfd,#dcdcdc);border:1px solid #c8c8c8;border-radius:2px;box-shadow:0 2px 4px rgba(0,0,0,.15);font-weight:700;font-size:16.5px;color:var(--deep-blue);display:flex;align-items:center;justify-content:center}
.btn-start::before{content:"";position:absolute;left:2px;top:14px;width:4px;height:18px;background:var(--green)}
/* newsletter */
.newsletter{left:93px;top:883px;width:756px;height:40px;border:1px solid #c8d0d6;border-radius:3px;background:linear-gradient(90deg,#dfe6eb,#f7f9fa 60%,#e8edf0)}
.newsletter .icon{position:absolute;left:0;top:0;width:50px;height:38px;background:#c3ccd3}
.newsletter .label{position:absolute;left:64px;top:11px;font-family:"Noto Serif",serif;font-size:11.5px;color:#333}
.newsletter .email-input{position:absolute;left:492px;top:8px;width:180px;height:22px;background:#fff;border:1px solid #d0d5d8;border-radius:10px}
.newsletter .send{position:absolute;left:677px;top:8px;width:63px;height:21px;border-radius:3px;background:linear-gradient(#9aa4ab,#6d777e);color:#fff;font-size:10px;display:flex;align-items:center;justify-content:center}
/* footer */
.wave{left:0;top:935px;width:960px;height:70px}
.footer{left:0;top:998px;width:960px;height:202px;background:var(--footer)}
.foot-title{top:1026px;font-family:"Play",sans-serif;font-weight:700;font-size:14.5px;color:#4c4c4c}
.foot-rule{top:1028px;width:1px;height:152px;background:#c9c9c9}
.clients{left:82px;top:1058px;width:165px;display:grid;grid-template-columns:82px 82px;row-gap:14px}
.clients span{font-weight:700;font-size:10px;color:#555;height:24px;display:flex;align-items:center;white-space:nowrap}
.about{left:289px;top:1054px;width:190px;font-size:11.5px;line-height:17.6px;font-weight:300;color:#555}
.about a{color:#333;text-decoration:none;font-weight:400}
.contact-field{position:absolute;left:552px;width:131px;background:#fff;border:1px solid #d4d4d4;font-size:10px;font-weight:300;color:#999;padding:4px 7px}
.foot-submit{left:552px;top:1158px;width:60px;height:22px;background:#8f8f8f;color:#fff;font-size:11.5px;display:flex;align-items:center;justify-content:center}
.follow{left:745px;top:1059px;display:grid;grid-template-columns:repeat(3,26px);gap:9px 6px}
.follow span{width:26px;height:26px;border-radius:50%;background:#8d8d8d;border:2px solid #bdbdbd}
</style>
</head>
<body>

<svg class="abs rays" viewBox="0 0 960 940" aria-hidden="true">
  <defs>
    <radialGradient id="glow" cx="0.58" cy="0.24" r="0.6">
      <stop offset="0" stop-color="#ffffff" stop-opacity=".85"/>
      <stop offset="1" stop-color="#ffffff" stop-opacity="0"/>
    </radialGradient>
  </defs>
  <g fill="#ffffff" opacity=".16">
    <polygon points="560,230 380,0 440,0"/>
    <polygon points="560,230 600,0 680,0"/>
    <polygon points="560,230 860,0 960,60"/>
    <polygon points="560,230 960,260 960,340"/>
    <polygon points="560,230 200,0 260,0"/>
    <polygon points="560,230 0,120 0,200"/>
    <polygon points="560,230 0,380 0,450"/>
  </g>
  <rect width="960" height="940" fill="url(#glow)"/>
  <g fill="#ffffff" opacity=".7">
    <ellipse cx="30" cy="400" rx="70" ry="26"/>
    <ellipse cx="930" cy="390" rx="70" ry="28"/>
    <ellipse cx="100" cy="455" rx="120" ry="30"/>
    <ellipse cx="880" cy="455" rx="120" ry="30"/>
  </g>
</svg>

<header>
  <div class="abs brand">
    <span class="brand-square"></span>
    <span class="brand-name">QUELVO</span>
  </div>
  <div class="abs social-top" aria-label="Social links">
    <span style="background:#2d5aa8"></span>
    <span style="background:#c9302c"></span>
    <span style="background:#3ab0e2"></span>
    <span style="background:#f0662a"></span>
  </div>
  <nav class="abs nav">
    <a href="#">Home</a><a href="#">Solutions</a><a href="#">Resources</a><a href="#">About</a><a href="#">Why Quelvo</a><a href="#">Contact</a>
  </nav>
</header>

<section class="hero">
  <div class="abs player">
    <div class="player-art" role="img" aria-label="Video slide illustration: SEO bar chart with a rising arrow, social media word cloud and search puzzle pieces"></div>
    <svg class="abs" style="left:165px;top:85px" width="36" height="36" viewBox="0 0 36 36" aria-hidden="true">
      <circle cx="18" cy="18" r="16" fill="#fff" stroke="#666" stroke-width="3"/>
      <polygon points="14,10 26,18 14,26" fill="#666"/>
    </svg>
    <div class="player-bar"><i></i></div>
    <span class="player-x"></span>
    <div class="ctrl" style="left:2px;width:20px">▶</div>
    <div class="ctrl" style="left:26px;width:54px">2:33 / 9:49</div>
    <div class="ctrl" style="left:84px;width:78px;justify-content:flex-start;padding-left:6px">◀<span style="display:inline-block;width:40px;height:8px;margin-left:4px;background:linear-gradient(90deg,#1d8fd1 55%,#bbb 55%)"></span></div>
    <div class="ctrl" style="left:282px;width:40px">SHARE ▾</div>
    <div class="ctrl" style="left:326px;width:16px">▦</div>
    <div class="ctrl ctrl-hd" style="left:346px;width:18px">HD</div>
  </div>
  <h1 class="abs hero-title">Is your Website Search Engine Optimized?</h1>
  <p class="abs hero-sub">Increase Traffic to your website and stay ahead<br>in ranking of the Search Engines.</p>
  <a class="abs btn-orange">Get Optimized Now</a>
</section>

<main>
  <div class="abs panel"></div>
  <h2 class="abs section-title" style="left:91px;top:404px">The way we do SEO</h2>

  <article class="abs card" style="left:88px">
    <h3 style="color:var(--orange)">Get Started Today</h3>
    <div class="art" role="img" aria-label="Golden SEO lettering illustration" style="background:linear-gradient(#f7d24a,#e3a317)"></div>
    <p>Lorem Ipsum is simply dummy text of the printing and type-setting industry.</p>
    <span class="pill" style="background:linear-gradient(#f6c48a,#e0954a)">More...</span>
  </article>
  <article class="abs card" style="left:354px">
    <h3 style="color:var(--green)">Build Your Site</h3>
    <div class="art" role="img" aria-label="Cart loaded with website building blocks illustration" style="background:linear-gradient(#e8ecef,#8b7a6a)"></div>
    <p>Lorem Ipsum is simply dummy text of the printing and type-setting industry.</p>
    <span class="pill" style="background:linear-gradient(#9ad24a,#6aa823)">More...</span>
  </article>
  <article class="abs card" style="left:624px">
    <h3 style="color:var(--blue)">Publish and Share</h3>
    <div class="art" role="img" aria-label="Social media word cloud illustration" style="background:radial-gradient(#6a8a3a,#3a3a3a 60%,#eee 75%)"></div>
    <p>Lorem Ipsum is simply dummy text of the printing and type-setting industry.</p>
    <span class="pill" style="background:linear-gradient(#a4dcf6,#5bb5e2)">More...</span>
  </article>

  <h2 class="abs section-title" style="left:97px;top:589px">How It Works</h2>
  <div class="abs how-art" role="img" aria-label="Illustration of a businessman presenting a rising chart on a board"></div>
  <div class="abs how-text">
    <p><b>Lorem Ipsum is simply dummy text of the printing and typesetting industry. Lorem Ipsum has been the industry's standard dummy text ever since the 1500s,</b> when an unknown printer took a galley of type and scrambled it to make a type specimen book. It has survived not only five centuries, but also the leap.</p>
    <p style="margin-top:14px">It was popularised in the 1960s with the release of Typorex sheets containing Lorem Ipsum passages, and more recently with desktop publishing software like Vellum Page-Setter including versions of Lorem Ipsum.</p>
  </div>
  <span class="abs pill" style="left:246px;top:746px;width:61px;background:linear-gradient(#9ad24a,#6aa823)">More...</span>

  <h2 class="abs section-title" style="left:645px;top:589px">Latest Quelvo News</h2>
  <div class="abs news-video" role="img" aria-label="News video still of a warehouse interior">
    <svg class="abs" style="left:77px;top:37px" width="48" height="48" viewBox="0 0 48 48" aria-hidden="true">
      <circle cx="24" cy="24" r="23" fill="#2a2928" opacity=".85"/>
      <polygon points="19,14 34,24 19,34" fill="#5a5856"/>
    </svg>
    <div class="abs" style="left:20px;top:112px;width:165px;height:3px;background:#888;border-radius:2px"></div>
  </div>

  <section>
    <p class="abs cta-line">Pointing You in the Right Direction!</p>
    <svg class="abs" style="left:608px;top:812px" width="32" height="24" viewBox="0 0 32 24" aria-hidden="true">
      <polygon points="0,8 18,8 18,1 31,12 18,23 18,16 0,16" fill="#1c7fd0"/>
    </svg>
    <a class="abs btn-start">Get Started Now</a>
  </section>

  <form class="abs newsletter">
    <div class="icon">
      <svg width="50" height="38" viewBox="0 0 50 38" aria-hidden="true">
        <rect x="10" y="8" width="30" height="20" fill="#fff" stroke="#222" stroke-width="2"/>
        <polyline points="10,8 25,20 40,8" fill="none" stroke="#222" stroke-width="2"/>
        <line x1="10" y1="28" x2="21" y2="18" stroke="#222" stroke-width="2"/>
        <line x1="40" y1="28" x2="29" y2="18" stroke="#222" stroke-width="2"/>
      </svg>
    </div>
    <span class="label">Enter your email valid address to subscribe our Monthly Newsletter</span>
    <span class="email-input"></span>
    <span class="send">Submit</span>
  </form>
</main>

<svg class="abs wave" viewBox="0 0 960 70" preserveAspectRatio="none" aria-hidden="true">
  <path d="M0,22 C120,10 200,14 320,18 C480,24 560,6 700,8 C820,10 900,14 960,4 L960,70 L0,70 Z" fill="#b7dbf3"/>
  <path d="M0,30 C120,18 220,22 330,26 C480,32 570,14 700,16 C820,18 900,22 960,12 L960,70 L0,70 Z" fill="var(--wave)"/>
</svg>

<footer class="abs footer"></footer>
<h3 class="abs foot-title" style="left:91px">Our Clients</h3>
<div class="abs clients">
  <span>Meridale Cells</span><span>Norvik</span>
  <span>Halvern Air</span><span>Roundway Tyres</span>
  <span>Zentra</span><span>Pellbrook's</span>
</div>
<span class="abs foot-rule" style="left:250px"></span>

<h3 class="abs foot-title" style="left:289px">About Us</h3>
<p class="abs about">&nbsp;Lorem ipsum dolor sit amet, con-sectetur adipisicing elit, sed do eiusmod tempor incididunt ut labore et dolore magna aliqua. Ut enim ad minim veniam.<br><a href="#">read more</a></p>
<span class="abs foot-rule" style="left:516px"></span>

<h3 class="abs foot-title" style="left:549px">Conact Us</h3>
<span class="contact-field" style="top:1060px;height:21px">Your Name</span>
<span class="contact-field" style="top:1086px;height:21px">Your Email</span>
<span class="contact-field" style="top:1114px;height:38px">Message</span>
<span class="abs foot-submit">Submit</span>
<span class="abs foot-rule" style="left:717px"></span>

<h3 class="abs foot-title" style="left:745px">Follow Us</h3>
<div class="abs follow" aria-label="Social links">
  <span></span><span></span><span></span>
  <span></span><span></span><span></span>
</div>

</body>
</html>
```